ultra-minimalist business card

front (black background, matte):

tarik b. hosseny
writer | photographer
get@tarikhosseny.com

back (white background, matte):

a picture speaks a thousand words;
a word draws a thousand pictures.

www.tarikhosseny.com

all text should be small (white or silver - as long as it shows against the black - on the front; black or gray - as long as it shows against the white - on the back).

feel free to get creative in terms of arrangement, alignment, and font type, but remember, the overall style is minimalist, so nothing too fancy, please.

thanks.

```html
<!DOCTYPE html>
<html lang="en">
<head>
<meta charset="utf-8">
<title>Tarik B. Hosseny — Business Card</title>
<link rel="stylesheet" href="https://fonts.googleapis.com/css2?family=Parisienne&family=Lato:wght@300&family=Open+Sans:wght@400;800&display=swap">
<style>
  :root {
    --page-bg: #ffffff;
    --card-black: #050203;
    --card-white: #ffffff;
    --gold: #f6b300;
    --gold-soft: #fdd680;
    --ink-light: #f2f2f2;
    --ink-silver: #d9d9d9;
    --ink-dark: #111111;
    --shadow: rgba(0, 0, 0, 0.28);
  }
  * { margin: 0; padding: 0; box-sizing: border-box; }
  html, body {
    width: 1046px;
    height: 1200px;
    overflow: hidden;
    background: var(--page-bg);
  }
  .canvas {
    position: relative;
    width: 1046px;
    height: 1200px;
  }
  .card {
    position: absolute;
    left: 125px;
    width: 793px;
    height: 452px;
    box-shadow: 0 6px 22px var(--shadow);
  }
  .card--front { top: 109px; background: var(--card-black); }
  .card--back { top: 632px; background: var(--card-white); }

  .card__name {
    position: absolute;
    left: 56px;
    top: 48px;
    font-family: "Parisienne", cursive;
    font-size: 78px;
    line-height: 1;
    color: var(--gold);
    white-space: nowrap;
  }
  .card__role {
    position: absolute;
    left: 57px;
    top: 150px;
    font-family: "Lato", sans-serif;
    font-weight: 300;
    font-size: 38px;
    line-height: 1;
    color: var(--ink-light);
    white-space: nowrap;
  }
  .card__rule {
    position: absolute;
    left: 57px;
    top: 217px;
    width: 48px;
    height: 5px;
    background: var(--gold);
  }
  .card__email {
    position: absolute;
    left: 57px;
    top: 365px;
    font-family: "Lato", sans-serif;
    font-weight: 300;
    font-size: 26px;
    line-height: 1;
    color: var(--ink-silver);
  }

  .quote__mark {
    position: absolute;
    font-family: "Open Sans", sans-serif;
    font-weight: 800;
    font-size: 190px;
    line-height: 1;
    color: var(--gold-soft);
  }
  .quote__mark--open { left: 78px; top: 124px; }
  .quote__mark--close { left: 636px; top: 200px; }
  .quote__text {
    position: absolute;
    left: 132px;
    top: 194px;
    font-family: "Open Sans", sans-serif;
    font-weight: 400;
    font-size: 29px;
    line-height: 38px;
    color: var(--ink-dark);
    white-space: nowrap;
  }
  .quote__line { display: block; }
  .quote__line + .quote__line { padding-left: 5px; }
</style>
</head>
<body>
<main class="canvas">
  <section class="card card--front" aria-label="Card front">
    <h1 class="card__name">Tarik b. hosseny</h1>
    <p class="card__role">writer | photographer</p>
    <div class="card__rule"></div>
    <p class="card__email">get@tarikhosseny.com</p>
  </section>

  <section class="card card--back" aria-label="Card back">
    <span class="quote__mark quote__mark--open" aria-hidden="true">&ldquo;</span>
    <blockquote class="quote__text">
      <span class="quote__line">A Picture Speaks A Thousand Words;</span>
      <span class="quote__line">A Word Draws A Thousand Pictures.</span>
    </blockquote>
    <span class="quote__mark quote__mark--close" aria-hidden="true">&rdquo;</span>
  </section>
</main>
</body>
</html>
```